A new website for Electrical Contractor Business

We are looking for a unique and new WordPress website design which would include 5 Pages - Home Page, Meet the Team, Our Services, Our Projects and Contact Us page.

The global theme for the website needs to be professional but simple to navigate as we cater for both business and home owner customers.

Our core business service is targeted around lighting from single room decorative to large office so the theme should incorporate this in some way.

The home page should include;
Our business logo, Contact number, Email address, small Image rotation box - Highlighting pervious projectsText box - With welcome message, chirpnet feed news reel/Customer feed back box.

I would also like to see a 2 boxes for the separate customer types we services. Business and Home Owner. each box will have a small image with a small text description with a link to the area of the services page relevant to that customer type.

Meet the team page -This will be introducing potential customers to the team so I would like it to include for each team member. Something like a small image and text area which will introduce an outline of the team members skills and abilities.

Our Services page This page will be outlining the different services on offer to the both customer types business and homeowner. Each service should have an image with text description of the service would good here.

Our projects page-Will include images of pervious projects and work we have completed along with a text area for the project description/ outliner.

Contact Us page - Should include a contact form which should include an option for the customer to quest us to call them back, also a selection box for them to inform us our how they found our details would be good.

Colour - The theme colours can be taken from the logo or feel free to impress with your own imagination.

Remember we are looking for a website that will interest our customers enough to except our services or be drawn further into the website.. So call to action links to other areas of the site/ contact page are welcome

Target Market(s)

Business - Office, warehousing and Large Store - lighting and Power
Home owner lighting and power

Coding

Coded - Design and coding required

Number of Pages Required

5+ page

Font styles to use
Serif
Sans Serif

Colors

Designer to choose colors to be used in the design.

Requirements
Must have
• Logo integrated into the website design - i.e. website colours which allow the logo to blend into the design.
Nice to have
• Custom but professional theme catering to business customers, but also show that we do provide services to home owners too.
Should not have
• Sorry am not interested in one oversized block image on rotation covering half the home page.. Images will be needed but not a single block over sized frame with not text, shape. Please use your imagination when considering this design

```html
<!DOCTYPE html>
<html lang="en">
<head>
<meta charset="utf-8">
<title>Brightline Electrical – Lighting and Power Solutions</title>
<link href="https://fonts.googleapis.com/css2?family=Roboto:ital,wght@0,300;0,400;0,500;0,700;0,900;1,400&display=swap" rel="stylesheet">
<style>
:root{
  --navy:#1f2f60;
  --orange:#f26a27;
  --grey-bg:#f4f4f4;
  --text:#333;
  --muted:#777;
  --tint:#dfe3ec;
  --chirp:#0aa7ee;
  --social-blue:#3b5a9e;
  --white:#fff;
}
*{box-sizing:border-box;margin:0;padding:0}
html,body{width:1200px;height:3412px;overflow:hidden}
body{font-family:"Roboto",Arial,sans-serif;color:var(--text);background:var(--white);position:relative}
section,header,nav,footer{position:absolute;left:0;width:1200px}
.abs{position:absolute}
.center{text-align:center}
.btn{position:absolute;display:flex;align-items:center;justify-content:center;color:var(--white);font-weight:700;font-size:11px;letter-spacing:.5px;text-transform:uppercase}
.btn-orange{background:var(--orange)}
.btn-navy{background:var(--navy)}
.lead{font-size:11px;line-height:18px;color:#555}

/* header */
.site-header{top:0;height:112px}
.call{left:170px;top:40px;font-size:15px;font-weight:700;color:var(--navy)}
.call span{color:var(--orange)}
.email{left:170px;top:65px;font-size:10.5px;color:#333}
.email span{color:var(--orange)}
.brand{left:480px;top:8px;width:240px;text-align:center}
.brand-mark{width:48px;height:48px;border-radius:50%;background:var(--navy);margin:0 auto 14px}
.brand-name{font-size:16px;font-weight:500;color:var(--navy);letter-spacing:1.5px;white-space:nowrap}
.tagline{right:167px;top:22px;font-size:10px;color:#333}
.tagline b{font-weight:700}
.callback{left:845px;top:47px;width:188px;height:39px;font-size:15px;font-weight:400;text-transform:none;letter-spacing:0}

/* nav */
.main-nav{top:112px;height:43px;background:var(--navy)}
.main-nav a{position:absolute;top:13px;color:var(--white);font-size:14px;text-decoration:none}
.main-nav a.active::after{content:"";position:absolute;left:-2px;right:-2px;top:27px;height:3px;background:var(--orange)}

/* hero */
.hero{top:155px;height:377px;background:linear-gradient(180deg,#c6d0d6 0%,#8b9aa6 45%,#4a5a8f 80%,#3d4c86 100%)}
.hero h1{position:absolute;top:155px;width:100%;text-align:center;font-size:31px;line-height:38px;font-weight:700;color:var(--white);text-shadow:0 2px 6px rgba(0,0,0,.45)}

/* welcome */
.welcome{top:532px;height:195px}
.welcome .hello{position:absolute;top:30px;width:100%;font-size:19px;font-weight:300}
.welcome h2{position:absolute;top:58px;width:100%;font-size:27px;font-weight:700;color:var(--orange)}
.welcome p{position:absolute;top:106px;left:190px;width:820px}

/* project blocks */
.projects{top:727px;height:485px;background:var(--grey-bg)}
.home-block{top:1212px;height:488px}
.section-title{position:absolute;width:100%;text-align:center;font-size:27px;font-weight:900;color:var(--navy)}
.tint-box{position:absolute;background:var(--tint)}
.photo{position:absolute}
.caption{position:absolute;width:300px;text-align:center;font-size:10.5px;line-height:18px;color:#333}
.caption a{color:var(--orange);text-decoration:none}
.dots{position:absolute;display:flex;gap:3px}
.dots i{width:7px;height:7px;border-radius:50%;background:var(--orange);display:block}
.dots i.on{background:var(--navy)}
.pitch{position:absolute;width:380px}
.pitch .kicker{font-size:16px;font-weight:400;color:#333}
.pitch h3{font-size:23px;font-weight:400;color:var(--navy);margin-top:10px}
.pitch p{font-size:10.5px;line-height:18px;color:var(--muted);margin-top:14px;padding-left:3px}
.contact-btn{width:118px;height:37px;letter-spacing:2px;font-size:10.5px}

/* testimonials */
.testimonials{top:1700px;height:560px;background:#f3f3f3;overflow:hidden}
.lamps{position:absolute;right:0;top:0;width:300px;height:360px;background:radial-gradient(ellipse at 60% 60%,#ffffff 0%,#ececec 55%,#f3f3f3 100%)}
.type{position:absolute;top:174px;width:400px;text-align:center;font-size:13px;color:#333}
.quote{position:absolute;top:201px;width:400px;height:143px;color:var(--white);font-style:italic;font-weight:400;font-size:13.5px;line-height:22.5px;text-align:center;padding:26px 30px}
.avatar{position:absolute;top:363px;width:82px;height:82px;border-radius:50%}
.person{position:absolute;top:456px;width:200px;text-align:center;font-size:10px;font-weight:500;text-transform:uppercase}

/* team */
.team{top:2260px;height:570px}
.card{position:absolute;top:168px;width:201px;height:287px;background:var(--white);box-shadow:0 0 8px rgba(0,0,0,.08)}
.card .photo{left:0;top:0;width:100%;height:204px}
.card h4{position:absolute;top:222px;width:100%;text-align:center;font-size:11.5px;font-weight:700;color:var(--navy)}
.card p{position:absolute;top:244px;width:100%;text-align:center;font-size:10.5px;color:#555}

/* social */
.social{top:2830px;height:230px;background:var(--grey-bg)}
.stat{position:absolute;top:0;width:300px;height:230px;color:var(--white);text-align:center}
.stat .dot{position:absolute;top:36px;left:144px;width:12px;height:12px;border-radius:50%;background:var(--white)}
.stat .label{position:absolute;top:78px;width:100%;font-size:9px;letter-spacing:1px}
.stat .count{position:absolute;top:94px;width:100%;font-size:37px;font-weight:900}
.stat .tag{position:absolute;top:195px;width:100%;font-size:10px}
.feed-label{left:367px;top:23px;font-size:8px;letter-spacing:1.5px;color:#aaa}
.feed-text{left:335px;top:66px;width:440px;font-size:14.5px;line-height:20px;color:#333}
.feed-text span{color:var(--orange)}
.feed-handle{left:366px;top:192px;font-size:10px;color:#333}
.feed-time{left:366px;top:206px;font-size:8px;color:#aaa}
.pager{left:765px;top:176px;width:75px;height:36px;border:1px solid #ccc;border-radius:18px;display:flex}
.pager span{flex:1;display:flex;align-items:center;justify-content:center}
.pager span+span{border-left:1px solid #ccc}

/* newsletter */
.newsletter{top:3060px;height:310px;background:var(--navy);color:var(--white)}
.newsletter h2{position:absolute;top:70px;width:100%;text-align:center;font-size:27px;font-weight:700}
.newsletter p{position:absolute;top:122px;width:100%;text-align:center;font-size:10.5px;color:#c8cde0}
.field{left:327px;top:173px;width:393px;height:41px;background:var(--white);color:#333;font-size:10.5px;padding:14px 16px}
.subscribe{left:720px;top:173px;width:116px;height:41px;font-size:10px}

/* footer */
.site-footer{top:3370px;height:42px}
.copy{left:168px;top:18px;font-size:8.5px;color:#333}
.foot-icons{right:162px;top:16px;display:flex;gap:13px}
.foot-icons i{display:block;width:10px;height:10px;border-radius:50%;background:var(--orange)}
</style>
</head>
<body>

<header class="site-header">
  <div class="abs call"><span>Call:</span> 555-010-2468</div>
  <div class="abs email"><span>Email</span> hello@brightline-electrical.example</div>
  <div class="abs brand">
    <div class="brand-mark"></div>
    <div class="brand-name">BRIGHTLINE ELECTRICAL</div>
  </div>
  <div class="abs tagline"><b>Unbeatable prices</b> and Service guaranteed!</div>
  <a class="btn btn-orange callback">Request a Call Back</a>
</header>

<nav class="main-nav">
  <a class="active" style="left:168px">Home</a>
  <a style="left:228px">Meet the Team</a>
  <a style="left:338px">Our Services</a>
  <a style="left:437px">Projects</a>
  <a style="left:510px">Contact us</a>
</nav>

<section class="hero" role="img" aria-label="Photo of a bright open-plan office lit by ceiling panels">
  <h1>Complete Lighting and Power Solution<br>for Home and Business</h1>
</section>

<section class="welcome center">
  <div class="hello">Welcome to</div>
  <h2>Brightline Electrical</h2>
  <p class="lead">Lorem ipsum dolor sit amet, consectetur adipiscing elit. Nunc vehicula dui quis nisi scelerisque tempor. Nulla accumsan nec nisl id blandit. Pellentesque non consequat nisl. Sed massa sapien, pulvinar in tempus ac, interdum id enim. Donec ornare velit eget odio iaculis mollis.</p>
</section>

<section class="projects">
  <h2 class="section-title" style="top:22px">Pervious Projects</h2>
  <div class="tint-box" style="left:299px;top:96px;width:233px;height:209px"></div>
  <div class="photo" role="img" aria-label="Photo of a modern office canteen with linear ceiling lights" style="left:201px;top:130px;width:296px;height:264px;background:linear-gradient(160deg,#4a4a4a 0%,#9a9690 45%,#c9b59a 100%)"></div>
  <div class="caption" style="left:199px;top:406px">Nulla accumsan nec nisl id blandit. Pellentesque non consequat nisl. <a>READ MORE</a></div>
  <div class="dots" style="left:330px;top:455px"><i></i><i class="on"></i><i></i><i></i></div>
  <div class="pitch" style="left:625px;top:140px">
    <div class="kicker">Lighting and Power Solution for</div>
    <h3>Business &amp; Office</h3>
    <p>Lorem ipsum dolor sit amet, consectetur adipiscing elit. Nunc vehicula dui quis nisi scelerisque tempor. Nulla accumsan nec nisl id blandit. Pellentesque non consequat nisl.</p>
    <p>Nulla erat erat, eleifend et massa eu, finibus dapibus sem. Mauris placerat, lorem in viverra suscipit, mi sapien dictum sapien, vitae porta nunc diam vel magna.</p>
  </div>
  <a class="btn btn-orange contact-btn" style="left:628px;top:343px">Contact us</a>
</section>

<section class="home-block">
  <div class="pitch" style="left:197px;top:76px">
    <div class="kicker">Lighting and Power Solution for</div>
    <h3>Home</h3>
    <p>Lorem ipsum dolor sit amet, consectetur adipiscing elit. Nunc vehicula dui quis nisi scelerisque tempor. Nulla accumsan nec nisl id blandit. Pellentesque non consequat nisl.</p>
    <p>Nulla erat erat, eleifend et massa eu, finibus dapibus sem. Mauris placerat, lorem in viverra suscipit, mi sapien dictum sapien, vitae porta nunc diam vel magna.</p>
  </div>
  <a class="btn btn-orange contact-btn" style="left:202px;top:278px">Contact us</a>
  <div class="tint-box" style="left:767px;top:53px;width:233px;height:208px"></div>
  <div class="photo" role="img" aria-label="Photo of a warm living room with pendant lights and a sofa" style="left:670px;top:86px;width:295px;height:264px;background:linear-gradient(160deg,#d9d3c6 0%,#a8714a 50%,#6c5a44 100%)"></div>
  <div class="caption" style="left:657px;top:366px">Nulla accumsan nec nisl id blandit. Pellentesque non consequat nisl. <a>READ MORE</a></div>
  <div class="dots" style="left:790px;top:415px"><i></i><i class="on"></i><i></i><i></i></div>
</section>

<section class="testimonials">
  <div class="lamps" role="img" aria-label="Row of hanging bulb pendant lamps"></div>
  <h2 class="section-title" style="top:50px">Testimonials</h2>
  <p class="lead abs center" style="left:190px;top:94px;width:820px">Lorem ipsum dolor sit amet, consectetur adipiscing elit. Nunc vehicula dui quis nisi scelerisque tempor. Nulla accumsan nec nisl id blandit. Pellentesque non consequat nisl. Sed massa sapien, pulvinar in tempus ac, interdum id enim. Donec ornare velit eget odio iaculis mollis.</p>
  <div class="type" style="left:184px">HOME OWNER</div>
  <div class="type" style="left:604px">BUSINESS OWNER</div>
  <div class="quote" style="left:184px;background:var(--orange)">“Lorem ipsum dolor sit amet, consectetur adipiscing elit. Nunc vehicula dui quis nisi scelerisque tempor. Nulla accumsan nec nisl id blandit. Pellentesque non consequat nisl.”</div>
  <div class="quote" style="left:604px;background:var(--navy)">“Lorem ipsum dolor sit amet, consectetur adipiscing elit. Nunc vehicula dui quis nisi scelerisque tempor. Nulla accumsan nec nisl id blandit. Pellentesque non consequat nisl.”</div>
  <div class="avatar" role="img" aria-label="Portrait of the home owner" style="left:341px;background:linear-gradient(#cfc4bb,#8c7468)"></div>
  <div class="avatar" role="img" aria-label="Portrait of the business owner" style="left:771px;background:linear-gradient(#d4ccc6,#7d6a60)"></div>
  <div class="person" style="left:282px;color:var(--navy)">Nadia Verhoef</div>
  <div class="person" style="left:712px;color:var(--orange)">Owen Castell</div>
  <a class="btn btn-orange" style="left:310px;top:486px;width:138px;height:34px;font-size:10px">View all services</a>
  <a class="btn btn-navy" style="left:746px;top:486px;width:138px;height:34px;font-size:10px">View all services</a>
</section>

<section class="team">
  <h2 class="section-title" style="top:53px">Our Team</h2>
  <p class="lead abs center" style="left:190px;top:96px;width:820px">Lorem ipsum dolor sit amet, consectetur adipiscing elit. Nunc vehicula dui quis nisi scelerisque tempor. Nulla accumsan nec nisl id blandit. Pellentesque non consequat nisl. Sed massa sapien, pulvinar in tempus ac, interdum id enim.</p>
  <div class="card" style="left:162px"><div class="photo" role="img" aria-label="Photo of electrician in yellow hard hat and hi-vis vest" style="background:linear-gradient(180deg,#f6f6f6 0%,#f0c64a 35%,#3b5ea8 100%)"></div><h4>RORY DELANEY</h4><p>Lorem ipsum dolor</p></div>
  <div class="card" style="left:384px"><div class="photo" role="img" aria-label="Photo of electrician in blue hard hat and checked shirt" style="background:linear-gradient(180deg,#f6f6f6 0%,#3d8fd6 30%,#6f7fa8 100%)"></div><h4>PAUL FERRAND</h4><p>Lorem ipsum dolor</p></div>
  <div class="card" style="left:610px"><div class="photo" role="img" aria-label="Photo of electrician in blue hard hat and navy vest" style="background:linear-gradient(180deg,#f6f6f6 0%,#4b8fd0 30%,#2f3e78 100%)"></div><h4>OWEN CASTELL</h4><p>Lorem ipsum dolor</p></div>
  <div class="card" style="left:836px"><div class="photo" role="img" aria-label="Photo of electrician in yellow hard hat and overalls" style="background:linear-gradient(180deg,#f6f6f6 0%,#efc54e 30%,#2c3346 100%)"></div><h4>TOMAS IVERLY</h4><p>Lorem ipsum dolor</p></div>
  <a class="btn btn-orange" style="left:531px;top:492px;width:138px;height:34px;font-size:10px">View all mambers</a>
</section>

<section class="social">
  <div class="stat" style="left:0;background:var(--chirp)"><i class="dot"></i><div class="label">CHIRPNET</div><div class="count">8899</div><div class="tag">#brightlineelectrical</div></div>
  <div class="abs feed-label">LATEST POSTS</div>
  <div class="abs feed-text">Nulla porttitor purus vel sollicitudin fermentum. Nam euismod nunc a tortor consectetur pellentesque. <span>#brightline #electrical</span></div>
  <div class="abs feed-handle">@brightline_electrical</div>
  <div class="abs feed-time">12 mins</div>
  <div class="abs pager">
    <span><svg width="8" height="10" viewBox="0 0 8 10"><path d="M6 1 2 5l4 4" fill="none" stroke="#888" stroke-width="1.4"/></svg></span>
    <span><svg width="8" height="10" viewBox="0 0 8 10"><path d="M2 1l4 4-4 4" fill="none" stroke="#888" stroke-width="1.4"/></svg></span>
  </div>
  <div class="stat" style="left:900px;background:var(--social-blue)"><i class="dot"></i><div class="label">PINBOARDLY</div><div class="count">10389</div><div class="tag">#brightlineelectrical</div></div>
</section>

<section class="newsletter">
  <h2>Subscribe to Our Newsletter</h2>
  <p>Lorem ipsum dolor sit amet, consectetur adipiscing elit. Nunc vehicula dui quis nisi scelerisque tempor. Nulla accumsan nec nisl id blandit. Pellentesque non consequat nisl.</p>
  <div class="abs field">Email Address</div>
  <a class="btn btn-orange subscribe">Subscribe</a>
</section>

<footer class="site-footer">
  <div class="abs copy">Copyright 2019 brightline-electrical.example All Right Reserved.</div>
  <div class="abs foot-icons"><i></i><i></i><i></i><i></i></div>
</footer>

</body>
</html>
```